Visitenkarten für Wahlärztin
Zielgruppe
Ich bin Ärztin für Allgemeinmedizin. Mein Schwerpunkt liegt auf Akupunktur und Manuelle Medizin. Als Wahlärztin sind meine Zielgruppe Privatpatienten - Primär Erwachsene, aber auch Kinder.
Aufgabenstellung
Logo (ev. nur Zeichen) und Informationen auf der Visitenkarte:
Dr. Gerlinde Wassmuthner
Ärztin für Allgemeinmedizin
Akupunktur
Manuelle Medizin
Lindauerstraße 7
4870 Lindenau am Kamp
praxis@dr-wassmuthner-beispiel.at
www.dr-wassmuthner-beispiel.at
Wahlärztin
Termin nach telefonischer Vereinbarung
Das Design soll das edle Logo mit Natürlichkeit/Leichtigkeit verbinden bzw. erden und ganzheitliche Medizin im verkörpern.

```html
<!DOCTYPE html>
<html lang="de">
<head>
<meta charset="utf-8">
<title>Visitenkarte Dr. Gerlinde Wassmuthner</title>
<link href="https://fonts.googleapis.com/css2?family=Alegreya:wght@500;700&family=Alegreya+Sans:wght@400;500&family=Fira+Sans:wght@600&display=swap" rel="stylesheet">
<style>
  :root {
    --backdrop: #eceeef;
    --card: #fbfbfb;
    --gold: #c9a13a;
    --gold-light: #e0c46e;
    --gold-dark: #a98222;
    --ink: #3b3c3e;
    --rule: #8a8b8d;
  }
  * { box-sizing: border-box; margin: 0; padding: 0; }
  html, body {
    width: 1200px; height: 721px; overflow: hidden;
    background: var(--backdrop);
  }
  .stage {
    width: 1200px; height: 721px;
    display: flex; align-items: center; justify-content: center; gap: 60px;
  }
  .card {
    position: relative;
    width: 520px; height: 336px;
    background: var(--card);
    box-shadow: 0 10px 30px rgba(0,0,0,.12);
    overflow: hidden;
    font-family: "Alegreya Sans", sans-serif;
    color: var(--ink);
  }
  .gold-fill { background: linear-gradient(100deg, var(--gold-dark), var(--gold-light) 45%, var(--gold) 75%, var(--gold-dark)); }

  /* front */
  .top-bar { position: absolute; left: 0; top: 34px; width: 300px; height: 16px; }
  .brand-mini {
    position: absolute; right: 28px; top: 26px;
    font-size: 14px; font-weight: 500; color: var(--gold-dark);
  }
  .name {
    position: absolute; left: 34px; top: 72px;
    font-family: "Alegreya", serif; font-weight: 700;
    font-size: 31px; color: var(--gold-dark);
  }
  .specialties {
    position: absolute; left: 34px; top: 116px;
    font-size: 15px; line-height: 19px;
  }
  .contact {
    position: absolute; left: 34px; top: 196px;
    list-style: none; font-size: 13px; line-height: 16px;
  }
  .contact li { display: flex; align-items: flex-start; gap: 10px; margin-bottom: 7px; }
  .contact svg { flex: none; width: 15px; height: 15px; margin-top: 1px; }
  .status-band {
    position: absolute; right: 0; bottom: 56px;
    width: 230px; height: 68px;
    clip-path: polygon(14% 0, 100% 0, 100% 100%, 0 100%);
    display: flex; align-items: center; justify-content: flex-end; padding-right: 22px;
  }
  .status-band span {
    font-family: "Fira Sans", sans-serif; font-weight: 600;
    font-size: 30px; color: #fff; letter-spacing: .5px;
  }

  /* back */
  .appointment {
    position: absolute; left: 250px; top: 70px; width: 240px;
  }
  .appointment p { font-size: 17px; line-height: 20px; margin-bottom: 24px; }
  .appointment .line { height: 1px; background: var(--rule); margin-bottom: 34px; }
  .brand-mark {
    position: absolute; left: 40px; bottom: 40px;
    display: flex; align-items: center; gap: 10px;
    font-size: 20px; font-weight: 500; color: var(--gold-dark);
  }
  .brand-mark .dot { width: 14px; height: 14px; border-radius: 50%; background: var(--gold); }
</style>
</head>
<body>
<main class="stage">
  <section class="card card-front" aria-label="Vorderseite">
    <div class="top-bar gold-fill"></div>
    <div class="brand-mini">Praxis Wassmuthner</div>
    <h1 class="name">Dr. Gerlinde Wassmuthner</h1>
    <p class="specialties">Ärztin für Allgemeinmedizin<br>Akupunktur<br>Manuelle Medizin</p>
    <ul class="contact">
      <li>
        <svg viewBox="0 0 16 16" fill="none" stroke="#3b3c3e" stroke-width="1.4"><path d="M8 15s5-5.2 5-8.5A5 5 0 0 0 3 6.5C3 9.8 8 15 8 15z"/><circle cx="8" cy="6.5" r="1.8"/></svg>
        <span>Lindauerstraße 7<br>4870 Lindenau am Kamp</span>
      </li>
      <li>
        <svg viewBox="0 0 16 16" fill="#3b3c3e"><path d="M4.2 1.5l2 3-1.3 1.6a8 8 0 0 0 5 5l1.6-1.3 3 2-1 2.4C8 14.5 1.5 8 1.8 2.5z"/></svg>
        <span>+43 660 248 17 93</span>
      </li>
      <li>
        <svg viewBox="0 0 16 16" fill="none" stroke="#3b3c3e" stroke-width="1.3"><rect x="1.5" y="3.5" width="13" height="9"/><path d="M1.5 3.5L8 9l6.5-5.5"/></svg>
        <span>praxis@dr-wassmuthner-beispiel.at</span>
      </li>
      <li>
        <svg viewBox="0 0 16 16" fill="none" stroke="#3b3c3e" stroke-width="1.2"><circle cx="8" cy="8" r="6.5"/><ellipse cx="8" cy="8" rx="3" ry="6.5"/><path d="M1.5 8h13M2.5 4.7h11M2.5 11.3h11"/></svg>
        <span>www.dr-wassmuthner-beispiel.at</span>
      </li>
    </ul>
    <div class="status-band gold-fill"><span>Wahlärztin</span></div>
  </section>

  <section class="card card-back" aria-label="Rückseite">
    <div class="appointment">
      <p>Termin nach<br>telefonischer Vereinbarung</p>
      <div class="line"></div>
      <div class="line"></div>
      <div class="line"></div>
    </div>
    <div class="brand-mark"><span class="dot"></span>Praxis Wassmuthner</div>
  </section>
</main>
</body>
</html>
```